Business Card Design Project - IT Company

CLOUD IT company working with medium to large corporate clients requires 2 sided Business Card design.

Strong, Professional and modern is what I am looking for.

The Logo JPG attached has all the colour palette options. which consist of Red and Silver on various backgrounds

Preferred option for the Back of card is either Silver Text on Red or Silver Text on Black. Though this is not concrete. Surprise me.

Logo must be prominent along with Contact details of the staff member

Tagline can be all Capitals " CLOUD MANAGED SERVICES"

I will look to provide feedback and tweaks to get the right design so it should be a fun process.

I will provide the layered files to the top few contenders.

Reason: Leaving the door open for some creativity. Don't forget this is an technology company. .

Target Market(s)

Leaders, decision makers, CEOs, CIOs,

Industry/Entity Type

Business

Requirements
Must have
• Data must have is

Company Name: Brelquist
Tagline: Cloud Managed Services

No Particular order

First Name Last name
Director
Mobile 0477 555 019
www.brelquist-example.com
First.Lastname@brelquist-example.com
Suite 7, 48 Wexmoor Lane, Sydney NSW 2000

```html
<!DOCTYPE html>
<html lang="en">
<head>
<meta charset="utf-8">
<title>Brelquist Business Card</title>
<link href="https://fonts.googleapis.com/css2?family=Play:wght@400;700&display=swap" rel="stylesheet">
<style>
  :root {
    --page: #e4e4e4;
    --red-dark: #6e0a0c;
    --red: #a3161a;
    --black: #111111;
    --black-soft: #2a2a2a;
    --silver: #cfcfcf;
    --silver-light: #f2f2f2;
    --silver-mid: #9c9c9c;
    --label: #8a8a8a;
    --detail: #bdbdbd;
  }
  * { margin: 0; padding: 0; box-sizing: border-box; }
  html, body { width: 1200px; height: 861px; overflow: hidden; }
  body {
    background: var(--page);
    font-family: "Play", sans-serif;
    position: relative;
  }
  .card {
    position: absolute;
    width: 540px;
    height: 310px;
    overflow: hidden;
    box-shadow: 0 10px 30px rgba(0,0,0,0.25);
  }
  .card-back { left: 40px; top: 275px; background: linear-gradient(135deg, var(--red) 0%, var(--red-dark) 100%); }
  .card-front { left: 620px; top: 275px; background: linear-gradient(135deg, var(--black-soft) 0%, var(--black) 70%); }
  .card-edges { position: absolute; inset: 0; width: 100%; height: 100%; }
  .brand {
    position: absolute;
    display: flex;
    align-items: center;
    gap: 12px;
  }
  .brand-mark {
    width: 34px; height: 34px;
    border-radius: 50%;
    background: var(--silver);
  }
  .brand-text { display: flex; flex-direction: column; }
  .brand-name {
    font-weight: 700;
    font-size: 52px;
    line-height: 0.95;
    color: var(--silver);
  }
  .brand-tagline {
    font-weight: 700;
    font-size: 11.5px;
    letter-spacing: 0.6px;
    color: var(--silver);
    align-self: flex-end;
  }
  .card-back .brand { left: 100px; top: 118px; }
  .card-front .brand { left: 140px; top: 40px; }
  .card-front .brand-name { font-size: 44px; }
  .card-front .brand-tagline { font-size: 10px; }
  .card-front .brand-mark { width: 28px; height: 28px; }
  .person { position: absolute; left: 100px; top: 132px; }
  .person-name {
    font-weight: 700;
    font-size: 31px;
    letter-spacing: 1.5px;
    color: var(--silver);
    line-height: 1;
  }
  .person-role {
    font-weight: 700;
    font-size: 15px;
    letter-spacing: 1px;
    color: var(--silver-mid);
    margin-top: 4px;
  }
  .contact {
    position: absolute;
    left: 100px;
    top: 212px;
    display: grid;
    grid-template-columns: 72px auto;
    row-gap: 3px;
    font-size: 13px;
  }
  .contact dt { font-weight: 700; color: var(--label); }
  .contact dd { color: var(--detail); }
</style>
</head>
<body>
  <section class="card card-back" aria-label="Card back">
    <svg class="card-edges" viewBox="0 0 540 310" aria-hidden="true">
      <polygon points="460,0 540,0 540,120 485,60" fill="var(--silver)"/>
      <polyline points="505,38 540,74" fill="none" stroke="var(--red-dark)" stroke-width="9"/>
    </svg>
    <div class="brand">
      <span class="brand-mark"></span>
      <div class="brand-text">
        <span class="brand-name">Brelquist</span>
        <span class="brand-tagline">CLOUD MANAGED SERVICES</span>
      </div>
    </div>
  </section>

  <section class="card card-front" aria-label="Card front">
    <svg class="card-edges" viewBox="0 0 540 310" aria-hidden="true">
      <polygon points="470,0 540,0 540,125 490,62" fill="var(--silver)"/>
      <polyline points="510,40 540,74" fill="none" stroke="var(--black)" stroke-width="9"/>
      <polygon points="0,90 16,90 72,200 16,310 0,310" fill="var(--silver)"/>
      <polyline points="0,158 28,200 0,242" fill="none" stroke="var(--black)" stroke-width="9" stroke-linejoin="miter"/>
    </svg>
    <div class="brand">
      <span class="brand-mark"></span>
      <div class="brand-text">
        <span class="brand-name">Brelquist</span>
        <span class="brand-tagline">CLOUD MANAGED SERVICES</span>
      </div>
    </div>
    <div class="person">
      <p class="person-name">NAME SURNAME</p>
      <p class="person-role">DIRECTOR</p>
    </div>
    <dl class="contact">
      <dt>Address:</dt><dd>Suite 7, 48 Wexmoor Lane, Sydney NSW 2000</dd>
      <dt>Mobile:</dt><dd>0477 555 019</dd>
      <dt>Email:</dt><dd>name@brelquist-example.com</dd>
      <dt>Website:</dt><dd>www.brelquist-example.com</dd>
    </dl>
  </section>
</body>
</html>
```